Quick Straightforward Billboard Redesign

- Design billboard sized for 10 foot' x 36' foot width live area size and please include bleeds 6" around all sides
- Exact blue color match is imperative in headline, logo, phone number bubble or wherever used. C-83 / M-45 / Y-1 / K-0-
- What I hope to illustrate is that our company offers the best porch screening in the area area, in regards to quality, expertise, durability, storms proof, but we do not build screen porches.
- Current board is attached below from previous designer, and as you can see sizing was off, white space on edges make it appear to be sized incorrectly.
- I also attached my own little mock up idea well well if it helps, favorite image, logo, headline, etc and ideas perhaps on expanding or making this better?

Thanks so much!

Target Market(s)

Drivers and passengers, Southeastern NC, are of immense new construction and high end homes.

Industry/Entity Type

Construction

Colors
0054AA
0677BA
7BADD7
CADEEF
E8F1F8

Requirements
Must have
• Blue color matching
Nice to have
• Design spins or other thoughts on my little mock up

```html
<!DOCTYPE html>
<html lang="en">
<head>
<meta charset="utf-8">
<title>Harborline Screens Billboard</title>
<link href="https://fonts.googleapis.com/css2?family=Oswald:wght@500&display=swap" rel="stylesheet">
<style>
  :root {
    --backdrop: #4a4a4a;
    --panel: #ffffff;
    --brand-blue: #0a67b4;
    --brand-green: #13b04b;
    --photo-sky: #8fc3ea;
    --photo-ceiling: #eef1f4;
    --photo-floor: #d9d3c7;
    --photo-lawn: #8aa85a;
  }
  html, body {
    margin: 0;
    width: 1200px;
    height: 1001px;
    overflow: hidden;
    background: var(--backdrop);
  }
  /* 36 ft x 10 ft live area: 3.6 : 1 */
  .billboard {
    position: absolute;
    left: 30px;
    top: 342px;
    width: 1140px;
    height: 317px;
    display: flex;
    font-family: "Oswald", "Arial Narrow", sans-serif;
    font-weight: 500;
  }
  .message-panel {
    position: relative;
    width: 530px;
    height: 100%;
    background: var(--panel);
  }
  .brand {
    position: absolute;
    left: 82px;
    top: 40px;
    display: flex;
    align-items: center;
    gap: 8px;
    color: var(--brand-blue);
    font-size: 26px;
    line-height: 1;
    text-transform: uppercase;
  }
  .brand-mark {
    width: 20px;
    height: 20px;
    background: var(--brand-blue);
  }
  .headline {
    position: absolute;
    left: 82px;
    top: 96px;
    margin: 0;
    font-weight: 500;
    font-size: 48px;
    line-height: 50px;
    letter-spacing: -0.4px;
  }
  .headline-lead { display: block; color: var(--brand-blue); }
  .headline-tag { display: block; color: var(--brand-green); }
  .phone-pill {
    position: absolute;
    left: 80px;
    top: 212px;
    width: 290px;
    height: 57px;
    border-radius: 29px;
    background: var(--brand-blue);
    color: #fff;
    display: flex;
    align-items: center;
    justify-content: center;
    gap: 10px;
    font-size: 42px;
    line-height: 1;
  }
  .phone-icon { width: 22px; height: 22px; }
  .porch-photo {
    flex: 1;
    height: 100%;
    background: linear-gradient(180deg,
      var(--photo-ceiling) 0%, var(--photo-ceiling) 30%,
      var(--photo-sky) 38%, var(--photo-sky) 50%,
      var(--photo-lawn) 58%, var(--photo-floor) 70%, #c9c1b3 100%);
  }
</style>
</head>
<body>
  <div class="billboard">
    <section class="message-panel">
      <div class="brand"><span class="brand-mark"></span>Harborline Screens</div>
      <h1 class="headline">
        <span class="headline-lead">Screen your Porch</span>
        <span class="headline-tag">Built for the Coast</span>
      </h1>
      <div class="phone-pill">
        <svg class="phone-icon" viewBox="0 0 24 24" aria-hidden="true">
          <path fill="#fff" d="M6.6 10.8c1.4 2.8 3.8 5.1 6.6 6.6l2.2-2.2c.3-.3.7-.4 1-.2 1.1.4 2.3.6 3.6.6.6 0 1 .4 1 1V20c0 .6-.4 1-1 1C10.6 21 3 13.4 3 4c0-.6.4-1 1-1h3.5c.6 0 1 .4 1 1 0 1.3.2 2.5.6 3.6.1.3 0 .7-.2 1l-2.3 2.2z"/>
        </svg>
        <span class="phone-number">910.555.0142</span>
      </div>
    </section>
    <div class="porch-photo" role="img" aria-label="Photo of a covered screened porch with white ceiling fans, wicker lounge chairs on stone pavers, and a lake view beyond"></div>
  </div>
</body>
</html>
```